Building Referrer Relationships Booklet

4 page A4 booklet to give to potential professional referrers to establish a collaborative relationship.Needs to be bright, vibrant, colourful, friendly, inviting, in keeping with The Wren Clinic colours.
Want to provide potential referrer partners a great reason to choose to collaborate with us. They need to know who we are, what makes us different/appealing, and who we are looking for to connect with.
The final product should communicate high performance and connectedness.

Target Market(s)

professional medical allied health and fitness practitioners

Industry/Entity Type

Health

Requirements
Must have
• energetic, vibrant, engaging, inviting, images

```html
<!DOCTYPE html>
<html lang="en">
<head>
<meta charset="utf-8">
<title>The Wren Clinic – Referral Partnerships Booklet</title>
<link rel="stylesheet" href="https://fonts.googleapis.com/css2?family=Montserrat:wght@400;500;600;700;800&display=swap">
<style>
:root{
  --bg:#ffffff;
  --paper:#ffffff;
  --navy:#0f5aa6;
  --sky:#2f86dc;
  --band:#4d97e6;
  --ink:#1f2a3a;
  --muted:#5a6576;
  --orange:#f08a1c;
  --green:#1f7a32;
  --photo-a:#dfe7f1;
  --photo-b:#f3d6c9;
}
*{margin:0;padding:0;box-sizing:border-box}
html,body{width:1200px;height:4000px;overflow:hidden;background:var(--bg)}
body{font-family:"Montserrat",sans-serif;color:var(--ink);position:relative}
.spread{position:absolute;left:30px;width:1140px;height:806px;display:flex;box-shadow:0 0 0 1px #e3e6ea}
.spread--outer{top:1134px}
.spread--inner{top:2060px}
.page{position:relative;width:570px;height:806px;background:var(--paper);overflow:hidden}
.abs{position:absolute}
/* back cover */
.partners{left:0;top:0;width:436px;height:666px;background:var(--navy);color:#fff;padding:42px 26px 0 26px}
.partners h2{font-size:17px;font-weight:800;letter-spacing:.3px;margin-bottom:18px}
.partner{margin-bottom:17px}
.partner h3{font-size:12px;font-weight:700;display:flex;align-items:center;gap:6px}
.partner p{font-size:9.5px;line-height:1.35;padding-left:22px;margin-top:3px}
.dot{width:14px;height:14px;border-radius:50%;background:#fff;flex:none}
.tick{color:#9cc8ff;margin-right:3px}
.call{left:38px;top:694px;font-size:27px;font-weight:800;color:var(--green)}
.contact{left:38px;font-size:11px;color:var(--ink);display:flex;align-items:center;gap:6px}
.badges{left:300px;top:738px;width:250px;display:grid;grid-template-columns:repeat(3,1fr);gap:8px 10px}
.badge{height:20px;background:#c9d1dc;border-radius:3px}
/* front cover */
.brand{right:40px;top:14px;display:flex;align-items:center;gap:8px;color:var(--navy);font-weight:600;font-size:19px;line-height:1.05}
.brand-mark{width:44px;height:44px;background:var(--navy)}
.cover-photo{left:0;top:127px;width:570px;height:451px;background:linear-gradient(135deg,var(--photo-a),var(--photo-b) 55%,var(--photo-a))}
.cover-band{left:0;top:578px;width:570px;height:110px;background:var(--band);color:#fff;text-align:center;padding-top:28px}
.cover-band h1{font-size:32px;font-weight:700;letter-spacing:.5px}
.cover-band p{font-size:11px;letter-spacing:1.5px;margin-top:6px;font-weight:500}
.cover-lines{left:0;width:570px;text-align:center;font-size:10.5px;font-weight:700;letter-spacing:.4px}
.cover-web{left:0;top:758px;width:570px;text-align:center;font-size:13px;font-weight:700;letter-spacing:1.5px}
/* about */
.about{left:0;top:0;width:310px;height:480px;background:var(--sky);color:#fff;padding:28px 22px 0 30px}
.about h2,.section-title{font-size:15px;font-weight:700}
.value{margin-top:15px;padding-left:16px;position:relative}
.value::before{content:"";position:absolute;left:0;top:2px;width:9px;height:9px;border-radius:50%;background:#fff}
.value h3{font-size:11px;font-weight:700;color:var(--orange)}
.value p{font-size:8.5px;line-height:1.35;margin-top:2px}
.team{left:334px;top:28px;width:220px}
.section-title{color:var(--sky)}
.member{display:flex;gap:10px;margin-top:10px}
.member-photo{width:34px;height:38px;background:linear-gradient(#c7cfd9,#9aa6b5);flex:none}
.member-info{font-size:7px;line-height:1.3;color:var(--muted);margin-top:1px}
.member-name{font-size:8.5px;font-weight:700;color:var(--ink);margin-top:3px}
.member-role{font-size:7.5px;color:var(--muted)}
.passion{left:30px;top:505px;width:510px;font-size:15px;font-weight:800;color:var(--orange);line-height:1.3;letter-spacing:.3px;text-align:justify}
.top3{left:30px;top:590px;font-size:11px;font-weight:700;color:var(--sky);line-height:1.3}
.point{left:30px;width:520px}
.point h4{font-size:11px;font-weight:700;color:var(--orange)}
.point p{font-size:9px;color:var(--muted);margin-top:2px;letter-spacing:.3px}
/* method page */
.way-title{left:30px;top:28px}
.intro{left:30px;top:52px;width:510px;font-size:9px;line-height:1.35;color:var(--muted)}
.way-photo{left:60px;top:108px;width:445px;height:175px;background:linear-gradient(120deg,#cfe0ee,#f1ece8 50%,#e2e9f2)}
.col{width:240px}
.step-kicker{font-size:12px;font-weight:700;color:var(--orange)}
.step h4{font-size:11px;font-weight:700;color:var(--ink)}
.step .sub{font-size:10px;color:var(--ink)}
.step ul{list-style:none;margin-top:4px}
.step li{font-size:8.5px;line-height:1.35;color:var(--muted);padding-left:12px;position:relative}
.step li::before{content:"✓";position:absolute;left:0;color:var(--sky);font-weight:700}
</style>
</head>
<body>

<section class="spread spread--outer">
  <div class="page page--back">
    <div class="abs partners">
      <h2>REFERRAL PARTNERS REQUIRED:</h2>
      <div class="partner"><h3><span class="dot"></span>MASSAGE THERAPISTS</h3><p><span class="tick">✓</span>Deep tissue and remedial massage<br><span class="tick">✓</span>Therapeutic massage</p></div>
      <div class="partner"><h3><span class="dot"></span>FASCIAL THERAPISTS</h3><p><span class="tick">✓</span>Whole-body myofascial releases to reset the alignment of the whole body</p></div>
      <div class="partner"><h3><span class="dot"></span>PHYSIOTHERAPISTS</h3><p><span class="tick">✓</span>Pain relief, protect and strengthen both lower limb and upper limb</p></div>
      <div class="partner"><h3><span class="dot"></span>GP, SPORTS PHYSICIANS</h3><p><span class="tick">✓</span>General health, diagnostics, treatment support, prescription medications<br><span class="tick">✓</span>Specialist referrals</p></div>
      <div class="partner"><h3><span class="dot"></span>OSTEOPATHS AND CHIROPRACTORS</h3><p><span class="tick">✓</span>Mobilisation and manipulative therapy for the spinal column and limbs</p></div>
      <div class="partner"><h3><span class="dot"></span>DIETICIAN AND NUTRITIONISTS</h3><p><span class="tick">✓</span>DEXA scan for bone density/lean mass/fat mass<br><span class="tick">✓</span>Optimising gut health and nutrition - You are what you eat!</p></div>
      <div class="partner"><h3><span class="dot"></span>PSYCHOLOGISTS/PSYCHIATRISTS</h3><p><span class="tick">✓</span>Sometimes our physical body cannot get better until we optimise a healthy mind</p></div>
      <div class="partner"><h3><span class="dot"></span>PERSONAL TRAINERS, PILATES AND<br>YOGA INSTRUCTORS</h3><p><span class="tick">✓</span>Create awesome body strength, flexibility and resilience</p></div>
      <div class="partner"><h3><span class="dot"></span>SURGEONS</h3><p><span class="tick">✓</span>When conservative methods are ineffective, surgical intervention works well</p></div>
    </div>
    <div class="abs call">CALL US NOW : 555 010 2030</div>
    <div class="abs contact" style="top:738px">
      <svg width="11" height="9" viewBox="0 0 11 9"><rect x=".5" y=".5" width="10" height="8" fill="none" stroke="#0f5aa6"/><path d="M.5 .5 5.5 5 10.5 .5" fill="none" stroke="#0f5aa6"/></svg>
      info@wrenreferrals.com
    </div>
    <div class="abs contact" style="top:758px">
      <svg width="11" height="11" viewBox="0 0 11 11"><circle cx="5.5" cy="5.5" r="5" fill="none" stroke="#1f7a32"/><path d="M.5 5.5h10M5.5.5c-3 3-3 7 0 10M5.5.5c3 3 3 7 0 10" fill="none" stroke="#1f7a32" stroke-width=".8"/></svg>
      www.wrenreferrals.com
    </div>
    <div class="abs badges">
      <div class="badge"></div><div class="badge"></div><div class="badge"></div>
      <div class="badge"></div><div class="badge"></div><div class="badge"></div>
    </div>
  </div>

  <div class="page page--front">
    <div class="abs brand"><span class="brand-mark"></span><span>Harbour<br>Podiatry<br>Network</span></div>
    <div class="abs cover-photo" role="img" aria-label="Photo of hands gently holding a pair of bare feet"></div>
    <div class="abs cover-band">
      <h1>REFERRAL PARTNERSHIPS</h1>
      <p>BECAUSE TOGETHER WE ACHIEVE MORE</p>
    </div>
    <div class="abs cover-lines" style="top:706px">WE ARE HERE TO HELP OUR CLIENTS GET BACK ON THEIR FEET</div>
    <div class="abs cover-lines" style="top:727px">LET'S COMBINE OUR SKILLSETS SO WE CAN ACHIEVE EVEN BETTER RESULTS.</div>
    <div class="abs cover-web">www.wrenreferrals.com</div>
  </div>
</section>

<section class="spread spread--inner">
  <div class="page page--about">
    <div class="abs about">
      <h2>ABOUT US:</h2>
      <div class="value"><h3>COURAGE</h3><p>Courage gives us the strength and confidence to take risks and embrace challenges.</p></div>
      <div class="value"><h3>INSPIRATION</h3><p>Inspiration is our energy, our fuel for success, the life force that feeds us as we grow and develop.</p></div>
      <div class="value"><h3>FUN</h3><p>Fun generates happiness, and we all function at our best when we are happy.</p></div>
      <div class="value"><h3>CREATIVE</h3><p>Creativity sets us up as an innovative, leading-edge business.</p></div>
      <div class="value"><h3>NOW</h3><p>Move means living the very best we can be and realise our true potential. We are not your average business, our service is not average, and our people are not average.</p></div>
      <div class="value"><h3>TEAM</h3><p>Team and in particular high-performance team means we perform at our very best. Great teamwork creates unity and we accomplish much more than each of us alone.</p></div>
    </div>

    <div class="abs team">
      <div class="section-title">OUR TEAM</div>
      <div class="member"><div class="member-photo" role="img" aria-label="Team member portrait"></div><div><div class="member-info">Podiatrist since 2009<br>Sports and biomechanics<br>Mon–Fri clinics</div><div class="member-name">DR MARCUS HALE</div><div class="member-role">(Principal Podiatrist)</div></div></div>
      <div class="member"><div class="member-photo" role="img" aria-label="Team member portrait"></div><div><div class="member-info">Podiatrist since 2012<br>Paediatric gait care<br>Tue–Sat clinics</div><div class="member-name">DR ELENA WARD</div><div class="member-role">(Senior Podiatrist)</div></div></div>
      <div class="member"><div class="member-photo" role="img" aria-label="Team member portrait"></div><div><div class="member-info">Podiatrist since 2015<br>Running injuries<br>Mon–Thu clinics</div><div class="member-name">DR NADIA COLE</div><div class="member-role">(Podiatrist)</div></div></div>
      <div class="member"><div class="member-photo" role="img" aria-label="Team member portrait"></div><div><div class="member-info">Podiatrist since 2017<br>Orthotic therapy<br>Wed–Sat clinics</div><div class="member-name">DR BEN TARRANT</div><div class="member-role">(Podiatrist)</div></div></div>
      <div class="member"><div class="member-photo" role="img" aria-label="Team member portrait"></div><div><div class="member-info">Clinic operations<br>Referral liaison<br>Mon–Fri</div><div class="member-name">LISA FENWICK</div><div class="member-role">(Practice Manager)</div></div></div>
      <div class="member"><div class="member-photo" role="img" aria-label="Team member portrait"></div><div><div class="member-info">Bookings and accounts<br>Front desk support<br>Mon–Sat</div><div class="member-name">JO CARVER</div><div class="member-role">(Front Office Administrator)</div></div></div>
    </div>

    <div class="abs passion">AT THE WREN CLINIC, WE ARE PASSIONATE ABOUT BUILDING STRONG POSTURAL FOUNDATIONS, FROM THE FEET UP</div>
    <div class="abs top3">THE TOP 3 THINGS OUR CLIENTS LOVE ABOUT US<br>(AND HOPEFULLY YOURS WILL TOO!):</div>
    <div class="abs point" style="top:630px"><h4>1. POSITIVE ENERGY, ENTHUSIASM AND OUTCOMES</h4><p>CLIENT AVERAGE SCORE +9 OUT OF 10</p></div>
    <div class="abs point" style="top:675px"><h4>2. TRUSTED LEADER IN THE PRACTICE OF PODIATRIC MEDICINE</h4><p>ESTABLISHED 1999, ELITE EXPERIENCE, LATEST HIGH-TECH EQUIPMENT</p></div>
    <div class="abs point" style="top:720px"><h4>3. FOCUS IS ON STRONG FEET, NOT JUST ORTHOTICS!</h4><p>BFT BAREFOOT TECHNOLOGY, WHOLE-BODY MYOFASCIAL, FOOT MANUAL THERAPIES</p></div>
  </div>

  <div class="page page--method">
    <div class="abs section-title way-title">THE WREN CLINIC WAY</div>
    <div class="abs intro">Our pathway to strengthen postural foundations, to create lasting changes for freedom of movement, and ultimately keep us going well beyond what we thought was possible (updated as research and tech changes).</div>
    <div class="abs way-photo" role="img" aria-label="Photo of a gloved practitioner examining a client's foot"></div>

    <div class="abs col step" style="left:30px;top:300px">
      <div class="step-kicker">FIX YOUR FEET</div>
      <h4>1. FIX THE PAIN</h4>
      <ul><li>Provide analgesia</li><li>Reduce inflammation</li><li>Corn/callus/foreign body removal</li><li>Improve/thickened toenail repair and maintenance</li><li>Surgery</li></ul>
    </div>
    <div class="abs col step" style="left:300px;top:300px">
      <div class="step-kicker">BIOHACK YOUR BODY</div>
      <div class="sub">(stability)</div>
      <h4>4. PROTECT THE WHOLE BODY</h4>
      <ul><li>Optimise Postural Alignment</li><li>Activate neuromuscular/reflexive balance stability</li><li>Customised corrective exercises</li><li>Improve cellular regeneration</li><li>Optimise nutrition/healthy gut</li><li>Optimise healthy mind</li></ul>
    </div>
    <div class="abs col step" style="left:30px;top:470px">
      <h4>2. PROTECT THE FEET</h4>
      <div class="sub">(reduce damage, optimise stability, promote healing)</div>
      <ul><li>Reduce tissue damage</li><li>Optimise Foot Posture</li><li>Activate neuromuscular/reflexive balance stability</li><li>Promote tissue repair/cellular regeneration</li></ul>
    </div>
    <div class="abs col step" style="left:300px;top:490px">
      <h4>5. STRENGTHEN THE WHOLE BODY</h4>
      <div class="sub">(strength, elasticity)</div>
      <ul><li>Strengthen the deep core (stabilisers)</li><li>Strengthen the outer core (mobilisers)</li><li>Increase fascial elasticity/strength</li><li>Increase functional strength</li><li>Increase endurance</li><li>Customised nutrition for specific performance</li><li>Improve psychological resilience</li></ul>
    </div>
    <div class="abs col step" style="left:30px;top:600px">
      <h4>3. STRENGTHEN THE FEET</h4>
      <div class="sub">(increase strength and resilience)</div>
      <ul><li>Strengthen intrinsics</li><li>Connect foot strength to core strength</li><li>Stimulate neuromuscular strength</li></ul>
    </div>
    <div class="abs col step" style="left:30px;top:690px">
      <h4>6. REPEAT CONSISTENTLY</h4>
      <ul><li>Our Elite Athlete Experience:</li><li>National Sports Academy</li><li>State Rugby Squad</li><li>Coastal Athletics Meet</li></ul>
    </div>
    <div class="abs col step" style="left:300px;top:704px">
      <ul><li>Westport Triathlon Series</li><li>Bayside Regional Games</li><li>Harbour Tennis Cup</li></ul>
    </div>
  </div>
</section>

</body>
</html>
```